PSD website for property company

Please read the brief thoroughly.

We are looking for a new website for a property group that does property acquisitions, property development and property management.
They buy, build and lease core inner city industrial assets in Sydney, Australia.
They also invest in residential developments.

Site menu
- Home page
- Property – sub menus include – Leasing ; Projects ; Investments ; Property Management
- Capital and finance
- About
- Contact

They like this website
https://www.vemlor.com.au/

They want the site to be clean, modern and bold.
They like few colors, even black and white is OK to submit

They have a logo and style guide and useable images here:
http://www.kruft.net/temp/PelworWeb2019.zip
The zip file is also attached to this project.
We have supplied some images to give you an idea, but we will also require you to provide at least 3 extra images from stock photos.
Use your imagination.

I am expecting a lot of similar designs, so be aware the photos you choose will be really important.
They want really 3 good stock photos used and supplied without charge.
Please not too generic, I repeat the quality of the photos is important.
You may provide several photos (but not in multiple submissions please) and we will choose the best three to be provided.

The winner will be selected on a single home page design and required to provide;
All photos use in original format without charge
A second ‘standard page’ template design based on the winning home page design

```html
<!DOCTYPE html>
<html lang="en">
<head>
<meta charset="utf-8">
<title>Pelwor – Property Development and Property Management</title>
<link href="https://fonts.googleapis.com/css2?family=Arimo:wght@400;700&display=swap" rel="stylesheet">
<style>
:root{
  --green:#405a23;
  --green-mid:#5d7a3c;
  --sage:#86a780;
  --sage-box:rgba(122,156,115,.92);
  --footer:#4a6130;
  --ink:#1e1e1e;
  --body:#555;
  --dark:#1d2022;
  --white:#fff;
}
*{margin:0;padding:0;box-sizing:border-box}
html,body{width:1200px;height:4800px;overflow:hidden}
body{font-family:"Arimo",Arial,sans-serif;color:var(--ink);background:var(--white);position:relative}
section,header,footer{position:absolute;left:0;width:1200px}
.abs{position:absolute}
.center{text-align:center}

/* hero */
.hero{top:0;height:700px;background:linear-gradient(180deg,#7d8a96 0%,#5e5f60 45%,#3a3430 75%,#4a4540 100%)}
.logo{left:143px;top:26px;font-size:44px;font-weight:700;letter-spacing:9px;color:var(--white)}
.nav{top:0;left:508px;display:flex;gap:0;font-size:14px;font-weight:700;color:var(--white)}
.nav a{color:var(--white);text-decoration:none;padding:44px 16px 0;height:82px}
.nav a.active{background:var(--sage);border-radius:0 0 16px 16px;padding:44px 14px 0}
.hero-box{left:280px;top:194px;width:640px;height:350px;border:3px solid var(--white);border-radius:30px;text-align:center;color:var(--white)}
.hero-title{font-size:96px;font-weight:700;letter-spacing:22px;margin-top:18px;line-height:1.1;padding-left:22px}
.hero-sub{font-size:40px;font-weight:700;line-height:52px;margin-top:10px}
.btn-sage{display:inline-block;background:var(--sage);color:var(--white);font-size:15px;font-weight:700;padding:11px 26px;margin-top:22px}
.dots{top:627px;left:568px;display:flex;gap:8px}
.dots span{width:16px;height:16px;border-radius:50%;border:2px solid var(--white)}
.dots span.on{background:var(--white)}

/* headings */
.sec-title{font-size:37px;font-weight:700;width:1200px;text-align:center}
.rule{height:3px;width:66px;left:567px;background:var(--green)}
.rule.light{background:var(--white)}

/* property */
.intro{left:175px;top:852px;width:850px;font-size:14.5px;line-height:29px;color:var(--body);text-align:center}
.card-img{width:425px;height:218px;background:linear-gradient(180deg,#aac3d8 0%,#d7dde2 45%,#6b5444 80%,#4a4a3e 100%)}
.card-img.b{background:linear-gradient(180deg,#8fb0d0 0%,#d9dfe5 50%,#cfc2b0 75%,#5d5246 100%)}
.card-img.c{background:linear-gradient(180deg,#6a86a6 0%,#9fb5c6 40%,#3e4a58 75%,#23282e 100%)}
.card-img.d{background:linear-gradient(180deg,#c4ccd2 0%,#a89274 45%,#6f6a52 75%,#3b4030 100%)}
.card-tab{width:36px;height:68px;background:#2c2e2c}
.badge{width:74px;height:74px;border-radius:50%;background:var(--green);border:4px solid var(--white);display:flex;align-items:center;justify-content:center}
.card-h{font-size:20px;font-weight:700}
.card-p{font-size:14px;line-height:26px;color:var(--body);width:380px}
.more{font-size:14px;font-weight:700;color:var(--green)}

/* capital */
.capital{top:1971px;height:643px;background:linear-gradient(100deg,#6b5a48 0%,#c9c4bc 35%,#e6e3de 55%,#b8a08a 75%,#d8d3cc 100%)}
.cap-box{left:143px;top:114px;width:418px;height:408px;background:var(--sage-box);color:var(--white);padding:0 35px}
.cap-box h2{font-size:40px;font-weight:400;margin-top:32px}
.cap-box .line{width:66px;height:3px;background:var(--white);margin:20px 0 20px}
.cap-box p{font-size:14.5px;line-height:29px}
.btn-ghost{display:inline-block;border:2px solid var(--white);font-size:14px;font-weight:700;padding:8px 22px;margin-top:22px}

/* testimonials */
.clients{top:2614px;height:609px;background:linear-gradient(180deg,#2a2d2f,#1b1e1f);color:var(--white)}
.quote-ico{width:46px;height:46px;border-radius:50%;background:var(--green);border:3px solid var(--white);display:flex;align-items:center;justify-content:center;font-size:34px;font-weight:700;line-height:1;padding-top:12px}
.t-box{width:274px;height:237px;border:2px solid var(--white);border-radius:10px;padding:26px 18px 0;text-align:center;font-size:14px;line-height:26px}
.t-box.fill{background:var(--sage);border-color:var(--sage)}
.t-box cite{display:block;font-style:normal;margin-top:8px}

/* news */
.news-card{width:283px;height:387px;background:var(--white);box-shadow:0 4px 14px rgba(0,0,0,.14)}
.news-img{margin:4px;width:275px;height:192px}
.news-body{padding:10px 20px}
.news-date{font-size:15px;display:flex;align-items:center;gap:8px}
.news-title{font-size:17px;font-weight:700;line-height:23px;margin-top:14px}
.news-text{font-size:13px;line-height:24px;color:var(--body);margin-top:10px}

/* contact */
.contact{top:3912px;height:742px;background:linear-gradient(180deg,#262a2c,#1c1f20);color:var(--white)}
.c-item{width:240px;text-align:center}
.c-ico{width:60px;height:60px;border-radius:50%;background:var(--green);margin:0 auto;display:flex;align-items:center;justify-content:center}
.c-item h3{font-size:20px;font-weight:400;margin-top:22px}
.c-item p{font-size:14px;line-height:26px}
.field{width:423px;height:38px;border:1px solid var(--white);font-size:12px;padding:12px 12px}
.field.msg{width:421px;height:205px;padding:14px 14px}
.submit{left:516px;top:617px;width:177px;height:41px;background:var(--green);font-size:20px;font-weight:700;display:flex;align-items:center;justify-content:center}

/* footer */
.site-footer{top:4654px;height:146px;background:var(--footer);color:var(--white)}
.social{width:30px;height:30px;border-radius:50%;border:2px solid var(--white)}
.copy{top:93px;width:1200px;text-align:center;font-size:14px}
</style>
</head>
<body>

<header class="hero" role="img" aria-label="Photo of a modern brick mid-rise building on a city street at dusk">
  <div class="abs logo">PELWOR</div>
  <nav class="abs nav">
    <a class="active">HOME</a><a>PROPERTY</a><a>CAPITAL AND FINANCE</a><a>ABOUT</a><a>CONTACT</a>
  </nav>
  <div class="abs hero-box">
    <div class="hero-title">PELWOR</div>
    <div class="hero-sub">Property Development And<br>Property Management</div>
    <span class="btn-sage">LEARN MORE</span>
  </div>
  <div class="abs dots"><span class="on"></span><span></span><span></span></div>
</header>

<section class="property" style="top:700px;height:1271px">
  <h2 class="abs sec-title" style="top:72px">PELWOR PROPERTY</h2>
  <div class="abs rule" style="top:130px"></div>
  <p class="abs intro" style="top:152px">Sed ut perspiciatis unde omnis iste natus error sit voluptatem accusantium doloremque laudantium, totam rem aperiam, eaque ipsa quae ab illo inventore veritatis et quasi architecto beatae vitae dicta sunt explicabo. Nemo enim ipsam voluptatem quia voluptas sit aspernatur aut odit aut fugit, sed quia consequuntur magni dolores eos qui ratione voluptatem</p>

  <!-- leasing -->
  <div class="abs card-tab" style="left:532px;top:515px"></div>
  <div class="abs card-img" style="left:143px;top:297px" role="img" aria-label="Photo of a brick building with arched windows"></div>
  <div class="abs badge" style="left:460px;top:498px"><svg width="36" height="36" viewBox="0 0 36 36" fill="none" stroke="#fff" stroke-width="2"><path d="M4 16 18 5l14 11"/><rect x="8" y="15" width="20" height="16"/><rect x="14" y="21" width="8" height="10"/></svg></div>
  <h3 class="abs card-h" style="left:143px;top:543px">LEASING</h3>
  <p class="abs card-p" style="left:143px;top:578px">Sed ut perspiciatis unde omnis iste natus error sit voluptatem accusantium doloremque laudantium, totam rem aperiam, eaque ipsa quae ab illo inventore veritatis et quasi architecto beatae</p>
  <div class="abs more" style="left:143px;top:695px">FIND OUT MORE &nbsp;&#10140;</div>

  <!-- projects -->
  <div class="abs card-tab" style="left:1021px;top:515px"></div>
  <div class="abs card-img b" style="left:632px;top:297px" role="img" aria-label="Photo of a modern mixed-use building on a street corner"></div>
  <div class="abs badge" style="left:949px;top:498px"><svg width="36" height="36" viewBox="0 0 36 36" fill="none" stroke="#fff" stroke-width="2"><rect x="8" y="6" width="20" height="26" rx="2"/><path d="M13 13h10M13 19h10M13 25h6"/><path d="M21 24l3 3 5-6"/></svg></div>
  <h3 class="abs card-h" style="left:632px;top:543px">PROJECTS</h3>
  <p class="abs card-p" style="left:632px;top:578px">Sed ut perspiciatis unde omnis iste natus error sit voluptatem accusantium doloremque laudantium, totam rem aperiam, eaque ipsa quae ab illo inventore veritatis et quasi architecto beatae</p>
  <div class="abs more" style="left:632px;top:695px">FIND OUT MORE &nbsp;&#10140;</div>

  <!-- investments -->
  <div class="abs card-tab" style="left:532px;top:979px"></div>
  <div class="abs card-img c" style="left:143px;top:761px" role="img" aria-label="Photo of glass office towers against a blue sky"></div>
  <div class="abs badge" style="left:460px;top:962px"><svg width="36" height="36" viewBox="0 0 36 36" fill="none" stroke="#fff" stroke-width="2"><rect x="6" y="22" width="6" height="9"/><rect x="15" y="16" width="6" height="15"/><rect x="24" y="10" width="6" height="21"/><path d="M6 14l8-6 6 4 10-7"/></svg></div>
  <h3 class="abs card-h" style="left:143px;top:1007px">INVESTMENTS</h3>
  <p class="abs card-p" style="left:143px;top:1042px">Sed ut perspiciatis unde omnis iste natus error sit voluptatem accusantium doloremque laudantium, totam rem aperiam, eaque ipsa quae ab illo inventore veritatis et quasi architecto beatae</p>
  <div class="abs more" style="left:143px;top:1159px">FIND OUT MORE &nbsp;&#10140;</div>

  <!-- property management -->
  <div class="abs card-tab" style="left:1021px;top:979px"></div>
  <div class="abs card-img d" style="left:632px;top:761px" role="img" aria-label="Photo of a curved residential complex with a plaza"></div>
  <div class="abs badge" style="left:949px;top:962px"><svg width="36" height="36" viewBox="0 0 36 36" fill="none" stroke="#fff" stroke-width="2"><rect x="6" y="8" width="16" height="22"/><path d="M10 13h8M10 18h8M10 23h5"/><circle cx="26" cy="24" r="5"/><path d="M26 19v-3M26 32v-3M21 24h-2M33 24h-2"/></svg></div>
  <h3 class="abs card-h" style="left:632px;top:1007px">PROPERTY MANAGEMENT</h3>
  <p class="abs card-p" style="left:632px;top:1042px">Sed ut perspiciatis unde omnis iste natus error sit voluptatem accusantium doloremque laudantium, totam rem aperiam, eaque ipsa quae ab illo inventore veritatis et quasi architecto beatae</p>
  <div class="abs more" style="left:632px;top:1159px">FIND OUT MORE &nbsp;&#10140;</div>
</section>

<section class="capital" role="img" aria-label="Photo of two colleagues reviewing charts at an office desk">
  <div class="abs cap-box">
    <h2>Capital and finance</h2>
    <div class="line"></div>
    <p>Sed ut perspiciatis unde omnis iste natus error sit voluptatem accusantium doloremque laudantium, totam rem aperiam, eaque ipsa quae ab illo inventore veritatis et quasi architecto beatae vitae dicta sunt explicabo. Nemo enim ipsam voluptatem quia voluptas sit aspernatur aut odit aut fugit, sed quia consequuntur magni dolores</p>
    <span class="btn-ghost">READ MORE</span>
  </div>
</section>

<section class="clients">
  <h2 class="abs sec-title" style="top:80px">WHAT OUR CLIENTS SAY</h2>
  <div class="abs rule light" style="top:143px"></div>

  <div class="abs quote-ico" style="left:263px;top:202px">&ldquo;</div>
  <div class="abs t-box" style="left:149px;top:268px">Sed ut perspiciatis unde omnis iste natus accusantium doloremque laudantium, totam rem aperiam, eaque ipsa quae ab illo inventore veritatis et quasi architecto beatae vitae dicta sunt explicabo.<cite>— Nemo enim ipsam</cite></div>

  <div class="abs quote-ico" style="left:576px;top:202px">&ldquo;</div>
  <div class="abs t-box fill" style="left:462px;top:268px">Sed ut perspiciatis unde omnis iste natus accusantium doloremque laudantium, totam rem aperiam, eaque ipsa quae ab illo inventore veritatis et quasi architecto beatae vitae dicta sunt explicabo.<cite>— Nemo enim ipsam</cite></div>

  <div class="abs quote-ico" style="left:887px;top:202px">&ldquo;</div>
  <div class="abs t-box" style="left:773px;top:268px">Sed ut perspiciatis unde omnis iste natus accusantium doloremque laudantium, totam rem aperiam, eaque ipsa quae ab illo inventore veritatis et quasi architecto beatae vitae dicta sunt explicabo.<cite>— Nemo enim ipsam</cite></div>
</section>

<section class="news" style="top:3223px;height:689px">
  <h2 class="abs sec-title" style="top:76px">LATEST NEWS</h2>
  <div class="abs rule" style="top:140px"></div>

  <article class="abs news-card" style="left:145px;top:190px">
    <div class="news-img" style="background:linear-gradient(135deg,#c58f62,#e8d9c8 55%,#a8805e)" role="img" aria-label="Photo of an architectural house model on plans"></div>
    <div class="news-body">
      <div class="news-date"><svg width="14" height="14" viewBox="0 0 14 14"><rect x="1" y="2" width="12" height="11" fill="none" stroke="#333" stroke-width="1.5"/><path d="M1 5h12" stroke="#333" stroke-width="1.5"/></svg>Feb 3, 2019</div>
      <div class="news-title">Sed ut perspiciatis unde omnis iste natus</div>
      <div class="news-text">Sed ut perspiciatis unde omnis iste natus error sit voluptatem accusantium domque laudantium, totam</div>
    </div>
  </article>

  <article class="abs news-card" style="left:458px;top:190px">
    <div class="news-img" style="background:linear-gradient(135deg,#5b6f8a,#dfe4ea 50%,#8a97a6)" role="img" aria-label="Photo of a businessman reviewing financial charts"></div>
    <div class="news-body">
      <div class="news-date"><svg width="14" height="14" viewBox="0 0 14 14"><rect x="1" y="2" width="12" height="11" fill="none" stroke="#333" stroke-width="1.5"/><path d="M1 5h12" stroke="#333" stroke-width="1.5"/></svg>Feb 3, 2019</div>
      <div class="news-title">Sed ut perspiciatis unde omnis iste natus</div>
      <div class="news-text">Sed ut perspiciatis unde omnis iste natus error sit voluptatem accusantium domque laudantium, totam</div>
    </div>
  </article>

  <article class="abs news-card" style="left:771px;top:190px">
    <div class="news-img" style="background:linear-gradient(180deg,#a9c5dd,#dfe6ea 30%,#7e9a5a 60%,#5e6e48)" role="img" aria-label="Photo of engineers on a construction site surrounded by trees"></div>
    <div class="news-body">
      <div class="news-date"><svg width="14" height="14" viewBox="0 0 14 14"><rect x="1" y="2" width="12" height="11" fill="none" stroke="#333" stroke-width="1.5"/><path d="M1 5h12" stroke="#333" stroke-width="1.5"/></svg>Feb 3, 2019</div>
      <div class="news-title">Sed ut perspiciatis unde omnis iste natus</div>
      <div class="news-text">Sed ut perspiciatis unde omnis iste natus error sit voluptatem accusantium domque laudantium, totam</div>
    </div>
  </article>
</section>

<section class="contact">
  <h2 class="abs sec-title" style="top:70px">CONTACT US</h2>
  <div class="abs rule light" style="top:130px"></div>

  <div class="abs c-item" style="left:130px;top:188px">
    <div class="c-ico"><svg width="26" height="30" viewBox="0 0 26 30"><path d="M13 1C6.5 1 2 6 2 12c0 8 11 17 11 17s11-9 11-17C24 6 19.5 1 13 1z" fill="#fff"/><circle cx="13" cy="12" r="4" fill="#405a23"/></svg></div>
    <h3>ADDRESS</h3><p>4100 Harlow St, #310<br>Fenwick Bay</p>
  </div>
  <div class="abs c-item" style="left:353px;top:188px">
    <div class="c-ico"><svg width="26" height="26" viewBox="0 0 24 24"><path d="M6.6 10.8a15 15 0 0 0 6.6 6.6l2.2-2.2c.3-.3.7-.4 1-.2 1.1.4 2.3.6 3.6.6.6 0 1 .4 1 1V20c0 .6-.4 1-1 1A17 17 0 0 1 3 4c0-.6.4-1 1-1h3.5c.6 0 1 .4 1 1 0 1.3.2 2.5.6 3.6.1.3 0 .7-.2 1z" fill="#fff"/></svg></div>
    <h3>PHONE</h3><p>612.40093.55100</p>
  </div>
  <div class="abs c-item" style="left:586px;top:188px">
    <div class="c-ico"><svg width="28" height="22" viewBox="0 0 28 22"><rect x="1" y="1" width="26" height="20" rx="2" fill="#fff"/><path d="M2 3l12 9 12-9" fill="none" stroke="#405a23" stroke-width="2"/></svg></div>
    <h3>EMAIL</h3><p>info@Pelwor.com</p>
  </div>
  <div class="abs c-item" style="left:825px;top:188px">
    <div class="c-ico"><svg width="30" height="30" viewBox="0 0 30 30"><circle cx="15" cy="15" r="13" fill="#fff"/><path d="M15 7v9l5 3" fill="none" stroke="#405a23" stroke-width="2.5"/></svg></div>
    <h3>HOURS</h3><p>Mon-Fri: 8:00 am-6:00 pm<br>Sat-Sun: 9:00 am-5:00 pm</p>
  </div>

  <div class="abs field" style="left:164px;top:380px">First Name</div>
  <div class="abs field" style="left:164px;top:436px">Last Name</div>
  <div class="abs field" style="left:164px;top:492px">Mobile Number</div>
  <div class="abs field" style="left:164px;top:548px">Email</div>
  <div class="abs field msg" style="left:613px;top:380px">Message</div>
  <div class="abs submit">SUBMIT</div>
</section>

<footer class="site-footer">
  <div class="abs social" style="left:529px;top:39px"></div>
  <div class="abs social" style="left:566px;top:39px"></div>
  <div class="abs social" style="left:603px;top:39px"></div>
  <div class="abs social" style="left:641px;top:39px"></div>
  <p class="abs copy">Copyright © Pelwor 2019. All rights reserved. | Privacy Policy</p>
</footer>

</body>
</html>
```